Wedding and event Photography company.

We need a business card design for a photography company based in Singapore named LumaVek. Our core service offering is wedding photojournalism. We would like to see minimalistic designs that use the colour white. The final design should communicate a sense of ease and reliability.

The attached are a couple of visual reference which i found over the web, i hope it will helps.

Project Brief Update (14th July 2014):
- Please refrain from using any images from the website for the design. The laws and regulations over here does not allow me to distribute my client's images. Thanks!

Target Market(s)

Young and middle aged adults aged 24 - 38. With money to spend =D

Industry/Entity Type

Business

Contact Information for Business Card

Name: Dax Pell
Designation: Head Photographer
Mobile: +65 84126079
Email: tan@lumavek.example
Website: www.lumavek.example

Font styles to use
Other font styles liked:
• Baskerville URW

Colors

Designer to choose colors to be used in the design.

Requirements
Must have
• Must include:
• - The brand LumaVek
• - The logo attached
• - Please help to place the brand LumaVek with the logo according to your preferences.
• - Services
• - Wedding Photography
• - Portraiture
• - Photojournalism
Nice to have
• Looking forward to an elegant and simple design. Please see attached examples!
• Please use Serif Fonts
Should not have
• Please refrain from using dark tones for the majority of the design.
• Please refrain from letterpress and embossing.

```html
<!DOCTYPE html>
<html lang="en">
<head>
<meta charset="utf-8">
<title>LumaVek Business Card</title>
<link rel="stylesheet" href="https://fonts.googleapis.com/css2?family=Libre+Baskerville:wght@400;700&family=Montserrat:wght@300&display=swap">
<style>
  :root {
    --backdrop: #2b2b2d;
    --card: #ffffff;
    --ink: #111111;
    --muted: #777777;
  }
  * { margin: 0; padding: 0; box-sizing: border-box; }
  html, body {
    width: 1200px;
    height: 931px;
    overflow: hidden;
    background: var(--backdrop);
  }
  .canvas {
    position: relative;
    width: 1200px;
    height: 931px;
  }
  .card {
    position: absolute;
    width: 640px;
    height: 366px;
    background: var(--card);
    box-shadow: 0 18px 40px rgba(0,0,0,0.45);
  }
  .card-frame {
    position: absolute;
    inset: 16px;
    border: 3px solid var(--ink);
  }
  .card-frame::after {
    content: "";
    position: absolute;
    inset: 4px;
    border: 1px solid var(--ink);
  }
  .card--contact { left: 60px; top: 70px; }
  .card--brand { left: 500px; top: 495px; }

  .person {
    position: absolute;
    left: 130px;
    top: 78px;
    display: flex;
    align-items: flex-end;
    gap: 14px;
  }
  .person-name {
    font-family: "Libre Baskerville", serif;
    font-size: 44px;
    font-weight: 400;
    letter-spacing: 2px;
    color: var(--ink);
  }
  .person-title {
    font-family: "Montserrat", sans-serif;
    font-weight: 300;
    font-size: 15px;
    letter-spacing: 1px;
    color: var(--muted);
    margin-bottom: 30px;
  }
  .contact {
    position: absolute;
    font-family: "Libre Baskerville", serif;
    font-size: 19px;
    letter-spacing: 1px;
    color: var(--ink);
    display: flex;
    align-items: center;
    gap: 6px;
  }
  .contact::before {
    content: "";
    width: 6px;
    height: 6px;
    border-radius: 50%;
    background: var(--ink);
  }
  .contact--web { left: 320px; top: 175px; }
  .contact--phone { left: 320px; top: 215px; }
  .contact--email { left: 60px; top: 280px; }

  .brand {
    position: absolute;
    inset: 0;
    display: flex;
    flex-direction: column;
    align-items: center;
    justify-content: center;
    gap: 14px;
  }
  .brand-name {
    font-family: "Libre Baskerville", serif;
    font-weight: 700;
    font-size: 58px;
    letter-spacing: 3px;
    color: var(--ink);
  }
  .brand-tagline {
    font-family: "Libre Baskerville", serif;
    font-size: 16px;
    letter-spacing: 0.5px;
    color: var(--ink);
  }
</style>
</head>
<body>
<main class="canvas">
  <section class="card card--contact">
    <div class="card-frame"></div>
    <div class="person">
      <h1 class="person-name">Dax Pell</h1>
      <p class="person-title">Head Photographer</p>
    </div>
    <p class="contact contact--web">www.lumavek.example</p>
    <p class="contact contact--phone">+6584126079</p>
    <p class="contact contact--email">tan@lumavek.example</p>
  </section>

  <section class="card card--brand">
    <div class="card-frame"></div>
    <div class="brand">
      <h2 class="brand-name">LumaVek</h2>
      <p class="brand-tagline">Wedding and event photography company</p>
    </div>
  </section>
</main>
</body>
</html>
```